Velanza Reggaeton Night

I'd like to create a flyer / poster for a reaggaeton Xmas party in London. The party will be titled "Velanza" and will be VIP for friends of friends only. The concept has to remain classy and stylish as I don't want it to be related to anything tropical at first glance. People attending the party will be a bit up-scale so the style is key. I am thinking of a black background and golden or silver letters, which give a bit of a "bling" look. Since the party will take place in Central London, I was thinking perhaps including something that relates to the city (Holbrine Cathedral, the Quillet, etc.). I have seen a few ideas and I am happy to send those over to illustrate a bit better what I am thinking of. Color wise, the theme could be very black and grey (for the London buildings) and only keep a few bright red colors if including London double decker buses or phone booths. Need to include something that gives the poster / flyer a Latin vibe as well.

Target Market(s)

25-35 year olds. Young professionals living in London. Latin American and European origins. People that enjoy dancing and like reggaeton music in particular.

Industry/Entity Type

Latin American Café

Requirements
Must have
• Must have the name of the party, VELANZA, as a big part of the flyer. Also the words "reggaeton party" or "reggaeton night". Something catchy. The date will be December 16 2017. Time will be 7pm to 3am. Location is Central London (Bank). I don't want to specify the location as I want it to be "secret" and only people with the ticket will be given the address.
Nice to have
• Nice to have something that resembles London but also the Latin, bling vibe of reggaeton music. Velanza means "flirt" in Spanish so I want the design to be flirty but elegant and very stylish. VELANZA could be written in Gold or Silver to make it stand-out. Could be made up of yellow light bulbs as well. And could include a rose to make it more flirty. See examples attached.
Should not have
• Typical tropical or Cuban type designs. I don't want anything too colorful as I want to keep it classy and stylish. Try to avoid people dancing in the flyer. Don't want a photo of sexy women in the flyer. Need to keep it classy.

```html
<!DOCTYPE html>
<html lang="en">
<head>
<meta charset="utf-8">
<title>Velanza Reggaeton Night</title>
<link rel="stylesheet" href="https://fonts.googleapis.com/css2?family=Anton&family=Teko:wght@600&family=Saira+Condensed:wght@600&display=swap">
<style>
  :root {
    --frame-grey: #5a5a5a;
    --night-black: #121212;
    --smoke-grey: #3a3a3a;
    --bling-gold: #f7c41a;
    --rose-red: #d8212a;
    --rose-deep: #7a0d12;
    --leaf-green: #2f6b2a;
  }
  * { margin: 0; padding: 0; box-sizing: border-box; }
  html, body {
    width: 887px;
    height: 1200px;
    overflow: hidden;
    background: var(--frame-grey);
  }
  .poster-frame {
    position: relative;
    width: 887px;
    height: 1200px;
    background: var(--frame-grey);
  }
  .poster {
    position: absolute;
    left: 59px;
    top: 59px;
    width: 769px;
    height: 1082px;
    overflow: hidden;
    background: var(--night-black);
  }
  .city-backdrop {
    position: absolute;
    inset: 0;
    background:
      radial-gradient(ellipse at 82% 22%, #4a4a4a 0%, transparent 42%),
      radial-gradient(ellipse at 12% 85%, #333 0%, transparent 40%),
      radial-gradient(ellipse at 70% 85%, #2e2e2e 0%, transparent 50%),
      linear-gradient(180deg, var(--smoke-grey) 0%, var(--night-black) 100%);
  }
  .rose {
    position: absolute;
    left: 112px;
    top: 280px;
    width: 175px;
    height: 170px;
  }
  .rose-leaves {
    position: absolute;
    left: 40px;
    top: 20px;
    width: 135px;
    height: 150px;
    border-radius: 50%;
    background: radial-gradient(circle at 55% 45%, var(--leaf-green) 0%, #1b3d18 65%, transparent 68%);
  }
  .rose-bloom {
    position: absolute;
    left: 0;
    top: 5px;
    width: 145px;
    height: 145px;
    border-radius: 50%;
    background: radial-gradient(circle at 45% 40%, var(--rose-red) 0%, #b0141c 55%, var(--rose-deep) 100%);
  }
  .headline {
    position: absolute;
    left: 384px;
    top: 532px;
    transform: translate(-50%, -50%) rotate(-49deg) scaleX(1.28);
    white-space: nowrap;
    font-family: "Anton", "Impact", sans-serif;
    font-weight: 400;
    font-size: 200px;
    line-height: 1;
    letter-spacing: 4px;
    color: var(--bling-gold);
  }
  .party-tagline {
    position: absolute;
    left: 458px;
    top: 758px;
    transform: translate(-50%, -50%) rotate(-49deg);
    font-family: "Teko", "Arial Narrow", sans-serif;
    font-weight: 600;
    font-size: 88px;
    line-height: 0.85;
    letter-spacing: 3px;
    color: var(--rose-red);
    text-align: center;
    white-space: nowrap;
  }
  .event-details {
    position: absolute;
    left: 0;
    right: 0;
    bottom: 14px;
    text-align: center;
    font-family: "Saira Condensed", "Arial Narrow", sans-serif;
    font-weight: 600;
    font-variant: small-caps;
    font-size: 37px;
    line-height: 1.15;
    letter-spacing: 1.5px;
    color: var(--bling-gold);
  }
</style>
</head>
<body>
  <div class="poster-frame">
    <main class="poster">
      <div class="city-backdrop" role="img" aria-label="Dark night photo of a London skyline with headphones and soft bokeh lights"></div>

      <div class="rose" role="img" aria-label="Red rose with green leaves">
        <div class="rose-leaves"></div>
        <div class="rose-bloom"></div>
      </div>

      <h1 class="headline">VELANZA</h1>

      <p class="party-tagline">REGGAETON<br>NIGHT</p>

      <footer class="event-details">
        <p>Date: December 16 2017. | Time: 7pm to 3am.</p>
        <p>Location: Central London</p>
      </footer>
    </main>
  </div>
</body>
</html>
```